Agricultural Consulting Website

Provide a modern yet business like website for my new Agriculture Consulting Business in Australia called FieldNorth. Whilst we are based in Australia we are targetting both domestic and international markets (especially in Asia). We are targetting corporate, small business, government and farmer clients. The design should compliment our logo also sourced through pixel harbor. The webiste should be easy for me to keep updated on a regular basis without the need to go back to the designer.

Industry/Entity Type

Business

Requirements
Must have
• clean crisp feel
• be modern yet business like
• be able to be updated by myself easily

```html
<!DOCTYPE html>
<html lang="en">
<head>
<meta charset="utf-8">
<title>FieldNorth — Agricultural Consulting</title>
<link href="https://fonts.googleapis.com/css2?family=Questrial&family=Arimo:wght@400;700&display=swap" rel="stylesheet">
<style>
:root{
  --brown:#5b2c0b;
  --brown-rule:#6a3510;
  --rust:#8a3f0c;
  --green:#5e9a0a;
  --green-dark:#4f7f08;
  --ink:#1c1c1c;
  --text:#2a2a2a;
  --muted:#555;
  --rule:#d8d8d8;
  --bg:#ffffff;
}
*{margin:0;padding:0;box-sizing:border-box}
html,body{width:1200px;height:1101px;overflow:hidden;background:var(--bg)}
body{position:relative;font-family:"Arimo",Arial,sans-serif;color:var(--text)}
.abs{position:absolute}

/* header */
.brand{left:121px;top:17px;display:flex;align-items:center;gap:8px;width:225px;white-space:nowrap}
.brand-mark{flex:none;width:56px;height:56px;background:var(--brown)}
.brand-name{font-family:"Questrial",sans-serif;font-size:31px;color:var(--brown);line-height:1}
.main-nav{left:354px;top:34px;display:flex;gap:17px;font-family:"Questrial",sans-serif;font-size:14.5px;color:var(--ink);white-space:nowrap}
.main-nav a{color:inherit;text-decoration:none}
.main-nav .current{color:var(--rust)}
.login{left:1051px;top:35px;width:43px;height:21px;background:var(--brown);color:#fff;font-family:"Questrial",sans-serif;font-size:14px;text-align:center;line-height:21px}
.header-rule{left:121px;top:91px;width:972px;height:4px;background:var(--brown-rule)}

/* hero */
.hero{left:121px;top:95px;width:972px;height:368px;display:flex}
.hero div{flex:1}
.hero .crop-basil{background:linear-gradient(160deg,#a6c56a,#2f6a1c)}
.hero .crop-pepper{background:linear-gradient(160deg,#8bbb2c,#2f5e0f)}
.hero .crop-wheat{background:linear-gradient(180deg,#9aa2a8 0%,#d99a2e 25%,#8a4b10 100%)}
.hero .crop-apple{background:linear-gradient(160deg,#b7d65a,#4d7a1a)}

/* feature cards */
.card{top:471px;width:321px;height:213px;overflow:hidden}
.card .photo{width:100%;height:100%}
.card .caption{position:absolute;left:0;bottom:0;width:100%;height:85px;background:rgba(98,46,8,.86);color:#fff;padding:9px 18px}
.card h3{font-family:"Arimo",sans-serif;font-size:17px;font-weight:700;line-height:20px;margin-bottom:2px}
.card p{font-size:14.5px;line-height:18px;color:#f1e6dc}
.card-mission{left:121px}
.card-vision{left:446px}
.card-event{left:772px}
.card-mission .photo{background:linear-gradient(180deg,#9ab7cf 0%,#6c7a4c 45%,#3f4a22 100%)}
.card-vision .photo{background:linear-gradient(180deg,#dfe8ee 0%,#8fb05a 35%,#c4d43a 75%,#6a8f22 100%)}
.card-event .photo{background:linear-gradient(180deg,#4f8fd0 0%,#a9c9e6 40%,#8a8f6a 100%)}

/* welcome */
.welcome-title{left:121px;top:717px;font-family:"Questrial",sans-serif;font-weight:700;font-size:28px;color:var(--brown);letter-spacing:.2px}
.welcome-lead{left:121px;top:759px;width:640px;font-size:18px;line-height:22px;color:var(--green)}
.welcome-photo{left:121px;top:824px;width:161px;height:151px;background:linear-gradient(180deg,#7fb2e0 0%,#d7e6f2 20%,#5ba130 32%,#2c6b16 100%)}
.welcome-body{left:299px;top:818px;width:453px;font-size:13px;line-height:22px;color:var(--text);text-align:justify}
.read-more{left:299px;top:956px;font-family:"Questrial",sans-serif;font-weight:700;font-size:17px;color:var(--green-dark)}

/* news */
.news-title{left:776px;top:716px;font-family:"Questrial",sans-serif;font-weight:700;font-size:24px;color:var(--green)}
.news-list{left:776px;top:760px;width:317px}
.news-item{padding-bottom:11px;margin-bottom:13px;border-bottom:1px solid var(--rule)}
.news-item:last-child{border-bottom:0}
.news-item h4{font-weight:400;font-size:17px;line-height:22px;color:var(--ink);margin-bottom:3px}
.news-item p{font-size:13px;line-height:22px;color:var(--text)}
.news-item .more{color:var(--rust)}

/* footer */
.footer-rule{left:121px;top:1040px;width:972px;height:1px;background:#9fbf5a}
.footer-nav{left:0;top:1055px;width:1214px;display:flex;justify-content:center;gap:18px;font-family:"Questrial",sans-serif;font-size:15px;color:var(--ink)}
.footer-nav .current{color:var(--rust)}
.copyright{left:0;top:1082px;width:1214px;text-align:center;font-family:"Questrial",sans-serif;font-size:13px;color:var(--muted)}
</style>
</head>
<body>

<header>
  <div class="abs brand">
    <span class="brand-mark"></span>
    <span class="brand-name">FieldNorth</span>
  </div>
  <nav class="abs main-nav">
    <a class="current" href="#">Home</a>
    <a href="#">About Us</a>
    <a href="#">Area of Expertise</a>
    <a href="#">Tours and Events</a>
    <a href="#">Focus</a>
    <a href="#">Gallery</a>
    <a href="#">Our Team</a>
    <a href="#">Contact Us</a>
  </nav>
  <div class="abs login">Login</div>
  <div class="abs header-rule"></div>
</header>

<section class="abs hero">
  <div class="crop-basil" role="img" aria-label="Rows of leafy basil plants in a field"></div>
  <div class="crop-pepper" role="img" aria-label="Pile of fresh green chilli peppers"></div>
  <div class="crop-wheat" role="img" aria-label="Ripe golden wheat stalks"></div>
  <div class="crop-apple" role="img" aria-label="Crate of green apples being harvested"></div>
</section>

<section>
  <article class="abs card card-mission">
    <div class="photo" role="img" aria-label="Consultants talking with a farmer beside a tractor"></div>
    <div class="caption">
      <h3>MISSION</h3>
      <p>Phasellus eleifend, magna non tincidunt accumsan, justo arcu cursus ipsum,</p>
    </div>
  </article>
  <article class="abs card card-vision">
    <div class="photo" role="img" aria-label="Farmer walking through green rolling farmland"></div>
    <div class="caption">
      <h3>VISION</h3>
      <p>Phasellus eleifend, magna non tincidunt accumsan, justo arcu cursus ipsum,</p>
    </div>
  </article>
  <article class="abs card card-event">
    <div class="photo" role="img" aria-label="Two farmers shaking hands under a blue sky"></div>
    <div class="caption">
      <h3>EVENT</h3>
      <p>Phasellus eleifend, magna non tincidunt accumsan, justo arcu cursus ipsum,</p>
    </div>
  </article>
</section>

<main>
  <h1 class="abs welcome-title">WELCOME TO FieldNorth</h1>
  <p class="abs welcome-lead">Lorem ipsum dolor sit amet consecteture adipicsing elit.Lorem ipsum dolor sit amet, consectetur adipiscing elit. Sed id tempus enim.</p>
  <div class="abs welcome-photo" role="img" aria-label="Crop rows stretching to the horizon"></div>
  <p class="abs welcome-body">Nam quis ligula a nibh fermentum venenatis vitae nec neque. Etiam non felis mi. Quisque feugiat, lectus non feugiat consectetur, purus ipsum lobortis nisl, a sollicitudin risus arcu elementum risus. Sed feugiat mollis neque. Suspend-isse potenti. Sed libero dui, consequat vel ultrices quis, faucibus iaculis nisi. Pellentesque sit amet eleifend augue. Fusce viverra nisl eu magna imperdiet euismod a vel tortor. Donec vulputate</p>
  <a class="abs read-more">READ MORE</a>

  <h2 class="abs news-title">Recent News</h2>
  <div class="abs news-list">
    <div class="news-item">
      <h4>Lorem ipsum dolor sit amet</h4>
      <p>Nam quis ligula a nibh fermentum venenatis vitae nec neque. Etiam non felis mi...<span class="more">more</span></p>
    </div>
    <div class="news-item">
      <h4>Lorem ipsum dolor sit amet</h4>
      <p>Nam quis ligula a nibh fermentum venenatis vitae nec neque. Etiam non felis mi...<span class="more">more</span></p>
    </div>
    <div class="news-item">
      <h4>Lorem ipsum dolor sit amet</h4>
      <p>Nam quis ligula a nibh fermentum venenatis vitae nec neque. Etiam non felis mi...<span class="more">more</span></p>
    </div>
  </div>
</main>

<footer>
  <div class="abs footer-rule"></div>
  <nav class="abs footer-nav">
    <span class="current">Home</span>
    <span>About Us</span>
    <span>Area of Expertise</span>
    <span>Tours and Events</span>
    <span>Focus</span>
    <span>Gallery</span>
    <span>Our Team</span>
    <span>Contact Us</span>
  </nav>
  <p class="abs copyright">© Copyright FieldNorth 2013. All rights reserved.</p>
</footer>

</body>
</html>
```